Marina Web Page

I'm looking for a visually engaging web page/layout that I can use as the basis for a website for my Marina. I need to include page content that can be stored and updated in an include file to allow someone to easily manage content without editing html or needing to understand html.

The business is a small marina and fishing center located on the Pamlico sound in eastern North Carolina right off the Intracoastal Waterway. We offer wet slips with power, water, and wifi and also have powered RV slips for camping available. The Marina sells fuel, beer, tackle/bait, and ice. The Marina also has an island style bar (The Gullwing Bar) and live music most weekends. The bar has a mascot named Dusty, short for captain, who is a black labradoodle know for diving to the bottom of the marina basin to retrieve oysters and rocks. Dusty could be incorporated as a minor design element but isn't a requirement.The marina caters to coastal sportsmen interested in sound fishing as well as offshore sport fishing. The Marina also offers fishing charters form a 32' Brinewood fishing boat w/ tuna tower.

The primary purpose of the initial version of the website is to communicate information about up coming events, music, bar specials etc... It will also be used to feature our services, fishing report and weather info, where we are located from both land and water, and a photo gallery.

Target Market(s)

Coastal sports enthusiast and the coastal boating community

Industry/Entity Type

Business

Requirements
Must have
• I would like animated menus incorporated into the page temple. It must also allow for the updating/storing of page content in a separate file to that an employee of the marina can update specials and events without having to understand or edit html.
Nice to have
• A photo gallery option that will present photos from a folder on the web server. Changing photos should be as easy as adding or deleting photos from the folder.

```html
<!DOCTYPE html>
<html lang="en">
<head>
<meta charset="utf-8">
<title>Sandpiper Cove Marina</title>
<link href="https://fonts.googleapis.com/css2?family=PT+Sans:wght@400;700&family=PT+Sans+Narrow:wght@400;700&display=swap" rel="stylesheet">
<style>
  :root {
    --sea-deep: #1f74b3;
    --sea-light: #3d9bd6;
    --brand-blue: #3a62b0;
    --nav-top: #6387c9;
    --nav-bottom: #3f66ad;
    --text-grey: #5a5a5a;
    --rule-grey: #d9d9d9;
    --card-white: #ffffff;
    --card-tint: #dfe8f7;
    --accent-orange: #e58a2c;
    --caption-bg: rgba(40, 40, 40, 0.72);
  }
  * { box-sizing: border-box; margin: 0; padding: 0; }
  html, body { width: 1046px; height: 1200px; overflow: hidden; }
  body {
    position: relative;
    font-family: "PT Sans", sans-serif;
    color: var(--text-grey);
  }
  .sea-backdrop {
    position: absolute; inset: 0;
    background: radial-gradient(ellipse at 50% 40%, var(--sea-light), var(--sea-deep) 75%);
  }
  .card {
    position: absolute; left: 156px; width: 733px;
    background: var(--card-white);
    border-radius: 6px;
  }
  .header-card { top: 70px; height: 400px;
    background: linear-gradient(var(--card-tint), var(--card-white) 50px); }
  .brand {
    position: absolute; left: 8px; top: -42px;
    display: flex; align-items: center; gap: 10px;
  }
  .brand-mark { width: 34px; height: 34px; border-radius: 50%; background: var(--accent-orange); margin-top: 94px; }
  .brand-name {
    margin-top: 94px;
    font-family: "PT Sans Narrow", sans-serif; font-weight: 700;
    font-size: 30px; color: var(--brand-blue); letter-spacing: 0.5px;
  }
  .social { position: absolute; left: 548px; top: 18px; display: flex; gap: 4px; }
  .social span { width: 20px; height: 20px; border-radius: 50%; background: var(--brand-blue); }
  .contact {
    position: absolute; left: 548px; font-size: 8px; text-transform: uppercase;
    display: flex; align-items: center; gap: 6px; color: #777;
  }
  .contact b { color: var(--brand-blue); font-weight: 700; }
  .contact.phone { top: 50px; }
  .contact.location { top: 75px; }
  .main-nav {
    position: absolute; left: 8px; top: 100px; width: 717px; height: 27px;
    border-radius: 4px;
    background: linear-gradient(var(--nav-top), var(--nav-bottom));
    display: flex; justify-content: space-around; align-items: center;
    font-family: "PT Sans Narrow", sans-serif; font-weight: 700;
    font-size: 9.5px; color: #fff; text-transform: uppercase;
  }
  .hero {
    position: absolute; left: 8px; top: 134px; width: 717px; height: 259px;
    border-radius: 6px; overflow: hidden;
    background: linear-gradient(180deg, #4a8cc9 0%, #1d4f93 40%, #163e7a 70%, #c9d6e6 100%);
  }
  .hero-caption {
    position: absolute; left: 0; top: 167px; width: 474px; height: 71px;
    background: var(--caption-bg); color: #fff; padding: 12px 14px;
  }
  .hero-caption h2 {
    font-family: "PT Sans Narrow", sans-serif; font-weight: 400;
    font-size: 15px; text-transform: uppercase; margin-bottom: 6px;
  }
  .hero-caption p { font-size: 6.4px; line-height: 13px; text-transform: uppercase; }
  .hero-arrows { position: absolute; right: 8px; bottom: 11px; display: flex; gap: 2px; }
  .hero-arrows span {
    width: 23px; height: 21px; background: rgba(40,40,40,0.5);
    display: flex; align-items: center; justify-content: center;
  }
  .content-card { top: 483px; height: 443px;
    background: linear-gradient(var(--card-tint), var(--card-white) 45px); }
  .section-title {
    font-family: "PT Sans Narrow", sans-serif; font-weight: 400;
    color: var(--brand-blue); text-transform: uppercase;
  }
  h1.section-title { font-size: 15px; }
  h2.section-title { font-size: 14px; }
  h3.section-title { font-size: 11.5px; font-weight: 700; }
  .body-text { font-size: 7.4px; line-height: 13.5px; }
  .welcome { position: absolute; left: 22px; top: 20px; width: 700px; }
  .welcome p { margin-top: 7px; }
  .about { position: absolute; left: 23px; top: 90px; width: 395px; }
  .about-photo { float: left; width: 151px; height: 78px; margin: 10px 16px 6px 0;
    background: linear-gradient(#5d7690, #2f4358 60%, #cfd8e0); }
  .about .intro { padding-top: 10px; }
  .testimonials { position: absolute; left: 442px; top: 90px; width: 272px; }
  .testimonials h4 { font-size: 8.5px; font-weight: 700; text-transform: uppercase; color: #555; margin: 10px 0 10px 2px; }
  .testimonial-body { display: flex; gap: 14px; }
  .testimonial-photo { width: 101px; height: 78px; flex: none; background: linear-gradient(#e5e3de, #b9a89a); }
  .testimonial-meta { margin: 12px 0 0 3px; font-size: 7.6px; color: var(--brand-blue); text-transform: uppercase; }
  .testimonial-meta span { margin: 0 12px; color: #555; }
  .pager { position: absolute; display: flex; gap: 3px; }
  .pager span { width: 12px; height: 14px; border: 1px solid #ccc; border-radius: 2px; background: #f4f4f4;
    display: flex; align-items: center; justify-content: center; }
  .btn {
    position: absolute; height: 20px; border-radius: 2px;
    background: linear-gradient(var(--nav-top), var(--nav-bottom));
    color: #fff; font-size: 7.6px; display: flex; align-items: center; justify-content: center;
  }
  .divider { position: absolute; left: 18px; top: 292px; width: 699px; border-top: 1px solid var(--rule-grey); }
  .gallery-title { position: absolute; left: 19px; top: 309px; }
  .gallery { position: absolute; left: 19px; top: 341px; display: flex; gap: 20px; }
  .gallery div { width: 123px; height: 80px; }
  .services-card { top: 938px; height: 145px; }
  .services-title { position: absolute; left: 22px; top: 13px; }
  .service { position: absolute; top: 42px; width: 150px; }
  .service p { margin-top: 4px; }
  .footer-card { top: 1098px; height: 55px; }
  .footer-nav { position: absolute; left: 18px; top: 23px; display: flex; font-size: 6.8px; text-transform: uppercase; color: #666; }
  .footer-nav span + span::before { content: "|"; margin: 0 14px; }
  .copyright { position: absolute; right: 14px; top: 23px; font-size: 6.8px; text-transform: uppercase; color: #666; }
</style>
</head>
<body>
  <div class="sea-backdrop" role="img" aria-label="Background photo of rippled blue sea water"></div>

  <header class="card header-card">
    <div class="brand">
      <span class="brand-mark"></span>
      <span class="brand-name">Sandpiper Cove Marina</span>
    </div>
    <div class="social" aria-label="Social links"><span></span><span></span><span></span></div>
    <div class="contact phone">
      <svg width="14" height="14" viewBox="0 0 14 14"><rect x="1" y="2" width="4" height="11" rx="1" fill="#999"/><rect x="6" y="4" width="7" height="9" rx="1" fill="#999"/><rect x="7.5" y="5.5" width="4" height="2" fill="#fff"/></svg>
      Call us: <b>( 1111 ) 111 111</b>
    </div>
    <div class="contact location">
      <svg width="11" height="14" viewBox="0 0 11 14"><path d="M5.5 0a5 5 0 0 1 5 5c0 3.5-5 9-5 9s-5-5.5-5-9a5 5 0 0 1 5-5z" fill="#999"/><circle cx="5.5" cy="5" r="2" fill="#fff"/></svg>
      Location: <b>Lat: 35° 12' 08" Long: -76° 41' 15"</b>
    </div>
    <nav class="main-nav">
      <span>Home</span><span>Events</span><span>Services</span><span>Gullwing Bar</span><span>Fishing</span><span>Weather</span><span>Where We Are</span>
    </nav>
    <div class="hero" role="img" aria-label="Photo of a white motor yacht speeding across deep blue water with hills behind">
      <div class="hero-caption">
        <h2>We also have a black labradoodle named as Dusty in our boat.</h2>
        <p>Our business is a small marina and fishing center. We offer wet slips with power, water, and wifi and also have powered RV slips for camping available. Our fishing charters form a 32' Brinewood fishing boat w/ tuna tower.</p>
      </div>
      <div class="hero-arrows">
        <span><svg width="7" height="11" viewBox="0 0 7 11"><path d="M6 1L1 5.5 6 10" stroke="#aaa" fill="none"/></svg></span>
        <span><svg width="7" height="11" viewBox="0 0 7 11"><path d="M1 1l5 4.5L1 10" stroke="#aaa" fill="none"/></svg></span>
      </div>
    </div>
  </header>

  <main class="card content-card">
    <section class="welcome">
      <h1 class="section-title">Welcome to Sandpiper Cove Marina</h1>
      <p class="body-text">Lorem Ipsum is simply dummy text of the printing and typesetting industry. Lorem Ipsum has been the industry's standard dummy text ever since the 1500s, when an unknown printer took a galley of type and scrambled it to make a type specimen book. It has survived not only five centuries, but also the leap into electronic typesetting, remaining essentially unchanged.</p>
    </section>

    <section class="about">
      <h3 class="section-title">About Sandpiper Cove Marina</h3>
      <div class="about-photo" role="img" aria-label="Photo of a sport fishing boat with tuna tower running at speed"></div>
      <p class="body-text intro">Lorem Ipsum is simply dummy text of the printing and typesetting industry. Lorem Ipsum has been the industry's standard dummy text ever since the 1500s, when an unknown printer took a galley of type and scrambled it to make a type specimen book. It has survived not only five centuries, but also the leap into electronic typesetting.</p>
      <p class="body-text" style="clear:both;padding-top:4px">Lorem Ipsum is simply dummy text of the printing and typesetting industry. Lorem Ipsum has been the industry's standard dummy text ever since the 1500s, when an unknown printer took a galley...</p>
    </section>
    <a class="btn" style="left:347px;top:254px;width:71px">View More</a>

    <section class="testimonials">
      <h3 class="section-title">Testimonials</h3>
      <h4>Powered RV slips for camping available</h4>
      <div class="testimonial-body">
        <div class="testimonial-photo" role="img" aria-label="Portrait photo of the customer giving the testimonial"></div>
        <p class="body-text">Lorem Ipsum is simply dummy text of the printing and typesetting industry. Lorem Ipsum has been the industry's standard dummy text ever since the 1500s, when an unknown printer since the 1500s, when an unknown printer.</p>
      </div>
      <p class="testimonial-meta">Wesley Hartman<span>|</span>20 Jul 2013</p>
    </section>
    <div class="pager" style="left:689px;top:92px"><span></span><span></span></div>
    <a class="btn" style="left:641px;top:254px;width:71px">View More</a>

    <div class="divider"></div>
    <h2 class="section-title gallery-title">Photo Gallery</h2>
    <div class="pager" style="left:689px;top:313px"><span></span><span></span></div>
    <div class="gallery">
      <div role="img" aria-label="Sport fishing boat on the water" style="background:linear-gradient(#5d7690,#2f4358 60%,#d4dde5)"></div>
      <div role="img" aria-label="Marina canal lined with docks and trees" style="background:linear-gradient(#8a8070,#4a4a3e 55%,#5c6470)"></div>
      <div role="img" aria-label="Black labradoodle lying on green grass" style="background:linear-gradient(#7a9a4a,#2a2a2a 45%,#6f9040)"></div>
      <div role="img" aria-label="Waterfront marina building with a boat at the dock" style="background:linear-gradient(#9fb7cf,#5a6b78 50%,#3f4a50)"></div>
      <div role="img" aria-label="White motor yacht on deep blue water" style="background:linear-gradient(#1c3f7a,#243f6e 50%,#18306a)"></div>
    </div>
  </main>

  <section class="card services-card">
    <h2 class="section-title services-title">Services</h2>
    <div class="pager" style="left:693px;top:16px"><span></span><span></span></div>
    <article class="service" style="left:23px">
      <h3 class="section-title">Dusty in our boat</h3>
      <p class="body-text">Lorem Ipsum is simply dummy text of the printing and typesetting industry. Lorem Ipsum has been the industry's...</p>
    </article>
    <article class="service" style="left:205px">
      <h3 class="section-title">Dusty in our boat</h3>
      <p class="body-text">Lorem Ipsum is simply dummy text of the printing and typesetting industry. Lorem Ipsum has been the industry's...</p>
    </article>
    <article class="service" style="left:386px">
      <h3 class="section-title">Dusty in our boat</h3>
      <p class="body-text">Lorem Ipsum is simply dummy text of the printing and typesetting industry. Lorem Ipsum has been the industry's...</p>
    </article>
    <article class="service" style="left:568px">
      <h3 class="section-title">Dusty in our boat</h3>
      <p class="body-text">Lorem Ipsum is simply dummy text of the printing and typesetting industry. Lorem Ipsum has been the industry's...</p>
    </article>
    <a class="btn" style="left:23px;top:109px;width:71px">Read More</a>
    <a class="btn" style="left:205px;top:109px;width:71px">Read More</a>
    <a class="btn" style="left:386px;top:109px;width:71px">Read More</a>
    <a class="btn" style="left:568px;top:109px;width:71px">Read More</a>
  </section>

  <footer class="card footer-card">
    <nav class="footer-nav">
      <span>Home</span><span>Events</span><span>Services</span><span>Gullwing Bar</span><span>Fishing</span><span>Weather</span><span>Where We Are</span>
    </nav>
    <p class="copyright">Copyrigts © 2013. Sandpiper Cove Marina. All rights reserved.</p>
  </footer>
</body>
</html>
```